Letterhead Design Project for online gaming site

We need a letterhead for a new online gaming company. The site is www.lunaroller.co

The logo is a gold colour and the site is similar in nature. Feel free to take a look at the landing page.

However the designer has free reign to do whatever they like with it.

OTHER CONTENT:

Telephone: 1300 746 315
Email: info@lunaroller.co
Web: www.lunaroller.co

Industry/Entity Type

It Company

```html
<!DOCTYPE html>
<html lang="en">
<head>
<meta charset="utf-8">
<title>LunaRoller.co Letterhead</title>
<link rel="stylesheet" href="https://fonts.googleapis.com/css2?family=Baloo+2:wght@800&family=Delius&display=swap">
<style>
  :root {
    --paper: #ffffff;
    --bronze-dark: #4e3b22;
    --bronze-mid: #8f7a52;
    --sun-yellow: #f7ef6e;
    --gold: #c9960e;
    --contact-ink: #7d5f43;
    --racing-tan: #c49a6b;
  }
  html, body {
    margin: 0;
    padding: 0;
    overflow: hidden;
    background: var(--paper);
  }
  .letterhead {
    position: relative;
    width: 848px;
    height: 1200px;
    overflow: hidden;
    background: var(--paper);
  }
  .letterhead__frame {
    position: absolute;
    inset: 0;
    width: 848px;
    height: 1200px;
  }
  .brand-name {
    position: absolute;
    left: 150px;
    top: 62px;
    margin: 0;
    font-family: "Baloo 2", sans-serif;
    font-weight: 800;
    font-size: 66px;
    line-height: 1;
    letter-spacing: -1px;
    color: var(--gold);
  }
  .contact {
    position: absolute;
    left: 616px;
    top: 24px;
    margin: 0;
    display: grid;
    grid-template-columns: 89px auto;
    row-gap: 4px;
    font-family: "Delius", cursive;
    font-size: 17px;
    line-height: 22px;
    color: var(--contact-ink);
  }
  .contact dt, .contact dd { margin: 0; }
  .racing-scene {
    position: absolute;
    left: 70px;
    top: 950px;
    width: 755px;
    height: 235px;
    background: var(--racing-tan);
    border-radius: 120px 120px 20px 20px / 90px 90px 20px 20px;
    opacity: 0.9;
  }
</style>
</head>
<body>
  <main class="letterhead">
    <svg class="letterhead__frame" viewBox="0 0 848 1200" aria-hidden="true">
      <defs>
        <linearGradient id="side-band-fill" x1="0" y1="0" x2="0" y2="1">
          <stop offset="0" stop-color="var(--bronze-dark)"/>
          <stop offset="0.22" stop-color="var(--bronze-mid)"/>
          <stop offset="0.55" stop-color="var(--sun-yellow)"/>
          <stop offset="1" stop-color="var(--sun-yellow)"/>
        </linearGradient>
        <linearGradient id="header-oval-fill" x1="0" y1="0" x2="1" y2="0">
          <stop offset="0" stop-color="var(--bronze-dark)"/>
          <stop offset="0.3" stop-color="var(--bronze-mid)"/>
          <stop offset="0.75" stop-color="var(--sun-yellow)"/>
          <stop offset="1" stop-color="var(--sun-yellow)"/>
        </linearGradient>
      </defs>
      <path class="side-band" d="M0 0 H82 C80 400 92 800 108 1195 L0 1200 Z" fill="url(#side-band-fill)"/>
      <path class="side-band__edge" d="M82 0 C80 400 92 800 108 1195" fill="none" stroke="#fffbe0" stroke-width="1.5" opacity="0.7"/>
      <ellipse class="header-oval" cx="306" cy="96" rx="285" ry="118" fill="url(#header-oval-fill)"/>
    </svg>

    <h1 class="brand-name">LunaRoller.co</h1>

    <dl class="contact">
      <dt>Phone:</dt><dd>1300 746 315</dd>
      <dt>Email:</dt><dd>info@lunaroller.co</dd>
      <dt>Web:</dt><dd>www.lunaroller.co</dd>
    </dl>

    <div class="racing-scene" role="img" aria-label="Tan silhouettes of a harness racer, a galloping racehorse with jockey, two greyhounds and a football running along the bottom of the page"></div>
  </main>
</body>
</html>
```